QORVEX needs a new business card!

QORVEX is a group of gaming enthusiasts who are looking for a new corporate business card.

The typeface should be modern and minimalist with attention paid to spacing between the letters and the letters 'qorvex' look relative to each other.

Should clean, crisp and minimalist - looking serious overall but with slight tweaks to the letters to make them look playful...

Black on white is fine.

Details on the card should include:
-the word 'qorvex'
-a job title (use any, for e.g. founder)
-a name (e.g. Ned Pascoe)
-phone number
-email address

For inspiration: http://brisk.tumvaleframe.example-cdn.com/wp-content/uploads/2013/07/lemo-1.jpg

Target Market(s)

Video gaming enthusiasts

Industry/Entity Type

Business

Requirements
Must have
• Black letter on white background.
The word "qorvex"
Nice to have
• Maybe use a conservative font like Gibraltar or Helvetica and tweaking each letter individually.

You can insert normal job titles under the "qorvex" typeface
Should not have
• Should not be cartoony or childish fonts. No colors.

```html
<!DOCTYPE html>
<html lang="en">
<head>
<meta charset="utf-8">
<title>QORVEX Business Card</title>
<link rel="stylesheet" href="https://fonts.googleapis.com/css2?family=Open+Sans:wght@400;600&display=swap">
<style>
  :root {
    --backdrop: #6f6668;
    --card: #f4f4f3;
    --ink: #111111;
    --ink-soft: #2b2b2b;
    --shadow: rgba(0, 0, 0, 0.35);
  }
  html, body {
    margin: 0;
    width: 1200px;
    height: 933px;
    overflow: hidden;
    background: var(--backdrop);
  }
  .stage {
    position: relative;
    width: 1200px;
    height: 933px;
  }
  .business-card {
    position: absolute;
    left: 180px;
    top: 226px;
    width: 840px;
    height: 480px;
    background: var(--card);
    box-shadow: 0 18px 40px var(--shadow);
    font-family: "Open Sans", sans-serif;
    color: var(--ink);
  }
  .brand {
    position: absolute;
    left: 64px;
    top: 36px;
  }
  .brand-name {
    margin: 0;
    font-size: 88px;
    font-weight: 600;
    line-height: 1;
    letter-spacing: -4px;
    color: var(--ink);
  }
  .job-title {
    margin: 6px 0 0 4px;
    font-size: 22px;
    font-weight: 400;
    color: var(--ink-soft);
  }
  .contact-list {
    position: absolute;
    right: 64px;
    bottom: 48px;
    margin: 0;
    padding: 0;
    list-style: none;
    font-size: 19px;
    line-height: 1.3;
    color: var(--ink);
  }
  .contact-item {
    display: flex;
    align-items: flex-start;
    gap: 12px;
  }
  .contact-icon {
    flex: 0 0 16px;
    width: 16px;
    height: 16px;
    margin-top: 4px;
    fill: var(--ink);
  }
</style>
</head>
<body>
<main class="stage">
  <section class="business-card">
    <header class="brand">
      <h1 class="brand-name">qorvex</h1>
      <p class="job-title">Manging Director</p>
    </header>

    <ul class="contact-list">
      <li class="contact-item">
        <svg class="contact-icon" viewBox="0 0 16 16" aria-hidden="true">
          <path d="M8 0a5.5 5.5 0 0 0-5.5 5.5C2.5 9.6 8 16 8 16s5.5-6.4 5.5-10.5A5.5 5.5 0 0 0 8 0zm0 7.8a2.3 2.3 0 1 1 0-4.6 2.3 2.3 0 0 1 0 4.6z"/>
        </svg>
        <span>Your Local Address<br>number goes here</span>
      </li>
      <li class="contact-item">
        <svg class="contact-icon" viewBox="0 0 16 16" aria-hidden="true">
          <path d="M3.6 1.2l2.2 2.9-1.4 1.6c.9 2 2.4 3.5 4.4 4.4l1.6-1.4 2.9 2.2-1.5 2.9C6.6 13.5 2.5 9.4 0.7 2.7z"/>
        </svg>
        <span>XXX-XXX -XXXX</span>
      </li>
      <li class="contact-item">
        <svg class="contact-icon" viewBox="0 0 16 16" aria-hidden="true">
          <path d="M1 3h14v1.2L8 9 1 4.2zM1 5.8l7 4.8 7-4.8V13H1z"/>
        </svg>
        <span>info@qorvex.com</span>
      </li>
      <li class="contact-item">
        <svg class="contact-icon" viewBox="0 0 16 16" aria-hidden="true">
          <path d="M8 0a8 8 0 1 0 0 16A8 8 0 0 0 8 0zm5.9 7.2h-2.6a12 12 0 0 0-.9-4.6 6.4 6.4 0 0 1 3.5 4.6zM8 1.6c.7.8 1.5 2.7 1.7 5.6H6.3C6.5 4.3 7.3 2.4 8 1.6zM5.6 2.6a12 12 0 0 0-.9 4.6H2.1a6.4 6.4 0 0 1 3.5-4.6zM2.1 8.8h2.6c.1 1.8.4 3.3.9 4.6a6.4 6.4 0 0 1-3.5-4.6zM8 14.4c-.7-.8-1.5-2.7-1.7-5.6h3.4c-.2 2.9-1 4.8-1.7 5.6zm2.4-1c.5-1.3.8-2.8.9-4.6h2.6a6.4 6.4 0 0 1-3.5 4.6z"/>
        </svg>
        <span>www.qorvex.com</span>
      </li>
    </ul>
  </section>
</main>
</body>
</html>
```